Polystyrene Recycling Material Flow

We need a diagram styled as an infographic that shows how polystyrene foam is recycled starting with a manufactured product, moving through the distribution process, waste material collection and reincorporation back into manufacturing. This is accomplished in different ways once the material is collected which needs to be clearly evident. The most important thing is for it to be simple enough to understand while still having a stylish look. The design can be with or without vector images or photography to depict the different stages. We are providing a very rudimentary 'sketch' of the information points and movement flow. Please see www.foamtradeguild.org (resources) to view our literature branding. The RGB & CMYK are attached.

Target Market(s)

Government Agencies, Brand Owners, Retailers, Recycling Industry

Industry/Entity Type

Packaging, Recycling, Manufacturing

Font styles to use
Sans Serif

Requirements
Must have
• Easy to Understand
Nice to have
• Images - either photography or vector illustrations - are optional. We have provided examples of both to show what could be used but are not required. Substituting your own interpretation of imagery is encouraged.
Should not have
• Outdated look.

```html
<!DOCTYPE html>
<html lang="en">
<head>
<meta charset="utf-8">
<title>Polystyrene Recycling Material Flow</title>
<link href="https://fonts.googleapis.com/css2?family=Montserrat:wght@500;600&display=swap" rel="stylesheet">
<style>
  :root{
    --panel:#5e8aa6;
    --olive:#a3a615;
    --gold:#b8900f;
    --orange:#f7a325;
    --brown:#5e2e1c;
    --ink:#111111;
    --white:#ffffff;
    --arrow:#5e8aa6;
  }
  *{margin:0;padding:0;box-sizing:border-box}
  html,body{width:848px;height:1200px;overflow:hidden;background:var(--white)}
  body{font-family:"Montserrat",sans-serif;position:relative}
  .canvas{position:relative;width:848px;height:1200px}
  .abs{position:absolute}
  .title{left:0;width:848px;top:8px;text-align:center;font-size:15px;font-weight:500;color:#222;letter-spacing:.3px}
  .panel{background:var(--panel);border-radius:8px}
  .label{color:var(--white);font-size:10px;font-weight:500;white-space:nowrap;transform:translate(-50%,-50%)}
  .label.sub{font-size:9px}
  .step{display:flex;align-items:center;justify-content:center;text-align:center;color:var(--white);border-radius:6px;font-weight:500}
  .step.major{font-size:16px;background:var(--olive);letter-spacing:.3px}
  .step.bar{font-size:12px;line-height:1.4}
  .olive{background:var(--olive)}
  .gold{background:var(--gold)}
  .orange{background:var(--orange)}
  .brown{background:var(--brown)}
  .art{border-radius:6px}
  .art-waste{background:linear-gradient(135deg,#e6e2d8,#8c9aa3)}
  .art-people{background:linear-gradient(135deg,#f2c9a0,#4b77a8)}
  .art-plant{background:linear-gradient(135deg,#d9dde0,#6a8fb5)}
  .art-line{background:linear-gradient(180deg,#6d7f8c,#4f9c8f 60%,#3a6fa0)}
  .art-yard{background:linear-gradient(135deg,#f1e6d0,#7cae5a)}
  .art-fleet{background:linear-gradient(135deg,#2bb3a5,#6da35a)}
  .art-foam{background:linear-gradient(135deg,#f3eee0,#c9b777 70%,#d8c04a)}
  .art-pellets{background:linear-gradient(135deg,#2a5d74 0%,#1e7fc2 35%,#d42b2b 70%,#e7b21c 100%)}
  .art-crane{background:linear-gradient(135deg,#f3a53a,#5b5f62)}
  svg.links{position:absolute;left:0;top:0}
</style>
</head>
<body>
<div class="canvas">

  <div class="abs title">EPS WASTE SOURCES</div>

  <!-- Sources panel -->
  <div class="abs panel" style="left:38px;top:39px;width:773px;height:225px"></div>

  <div class="abs art art-waste" role="img" aria-label="Illustration of a pile of household rubbish" style="left:116px;top:58px;width:89px;height:44px"></div>
  <div class="abs label" style="left:161px;top:118px">MUNCIPAL WASTE</div>
  <div class="abs label" style="left:424px;top:97px">MANUFACTURING WASTE</div>
  <div class="abs art art-line" role="img" aria-label="Photo of a sorting conveyor loaded with mixed plastic waste" style="left:313px;top:114px;width:223px;height:116px;border-radius:4px"></div>
  <div class="abs art art-people" role="img" aria-label="Illustration of people sorting waste into coloured recycling bins" style="left:653px;top:51px;width:89px;height:55px"></div>
  <div class="abs label" style="left:686px;top:118px">COMMERCIAL WASTE</div>

  <div class="abs label sub" style="left:105px;top:179px">CURBSIDE COLLECTION</div>
  <div class="abs label sub" style="left:225px;top:179px">DROP-OFF CENTERS</div>
  <div class="abs label sub" style="left:630px;top:179px">BACK HAULING</div>
  <div class="abs label sub" style="left:749px;top:179px">LOCALIZED DELIVERY</div>

  <div class="abs art art-people" role="img" aria-label="Illustration of a person placing items in a curbside bin" style="left:79px;top:192px;width:51px;height:68px"></div>
  <div class="abs art art-plant" role="img" aria-label="Illustration of a drop-off recycling station" style="left:195px;top:192px;width:65px;height:68px"></div>
  <div class="abs art art-plant" role="img" aria-label="Illustration of a worker returning materials on a back haul" style="left:592px;top:192px;width:72px;height:68px"></div>
  <div class="abs art art-people" role="img" aria-label="Illustration of a person delivering items to a local bin" style="left:735px;top:192px;width:45px;height:68px"></div>

  <!-- Collecting -->
  <div class="abs step major" style="left:354px;top:292px;width:142px;height:40px">COLLECTING</div>

  <!-- Compaction panel -->
  <div class="abs panel" style="left:53px;top:365px;width:388px;height:236px;border-radius:6px"></div>
  <div class="abs art art-fleet" role="img" aria-label="Illustration of a recycling truck with waste bags" style="left:185px;top:339px;width:120px;height:61px"></div>
  <div class="abs step major" style="left:171px;top:405px;width:142px;height:40px">COMPACTION</div>
  <div class="abs label" style="left:132px;top:502px">EXTURDED INGOT</div>
  <div class="abs label" style="left:347px;top:502px">HYDROLIC COMPRESSION</div>
  <div class="abs art art-people" role="img" aria-label="Illustration of a person feeding plastic into an extruder" style="left:86px;top:520px;width:92px;height:68px"></div>
  <div class="abs art art-plant" role="img" aria-label="Illustration of a hydraulic compression machine" style="left:315px;top:510px;width:82px;height:86px"></div>

  <!-- Regrind branch -->
  <div class="abs art art-crane" role="img" aria-label="Illustration of a crane grabbing scrap material" style="left:595px;top:318px;width:103px;height:92px"></div>
  <div class="abs step bar gold" style="left:508px;top:423px;width:277px;height:40px">REGRIND - MOLDER FACILITIES</div>

  <div class="abs panel" style="left:479px;top:510px;width:335px;height:204px;border-radius:6px"></div>
  <div class="abs step major" style="left:576px;top:536px;width:142px;height:40px">SHREDDING</div>
  <div class="abs art art-people" role="img" aria-label="Illustration of a person emptying material into a shredder bin" style="left:725px;top:520px;width:51px;height:65px"></div>
  <div class="abs label" style="left:547px;top:641px">HOMOGENIZATION</div>
  <div class="abs label" style="left:724px;top:641px">MIXING FOR CONSISTENCY</div>
  <div class="abs art art-plant" role="img" aria-label="Illustration of technicians blending material in a vessel" style="left:499px;top:651px;width:72px;height:60px"></div>
  <div class="abs art art-plant" role="img" aria-label="Illustration of scientists testing a sample" style="left:708px;top:657px;width:75px;height:54px"></div>
  <div class="abs step bar gold" style="left:508px;top:749px;width:277px;height:40px">RECYCLED CONTENT PACKAGING &lt;15%</div>

  <!-- Left column -->
  <div class="abs art art-people" role="img" aria-label="Illustration of people carrying recycled foam blocks" style="left:149px;top:643px;width:116px;height:74px"></div>
  <div class="abs step bar orange" style="left:70px;top:723px;width:277px;height:40px">RECYCLED CONTENT EPS RESIN</div>
  <div class="abs art art-yard" role="img" aria-label="Illustration of two people holding a go green sign" style="left:178px;top:775px;width:68px;height:64px"></div>
  <div class="abs step bar brown" style="left:70px;top:866px;width:277px;height:41px">RE-PELLETIZED WITH BLOWING AGENT</div>
  <div class="abs step bar gold" style="left:70px;top:967px;width:277px;height:47px">EXPANDED POLYSTYRENE<br>PACKAGING &amp; BUILDING PRODUCTS</div>
  <div class="abs art art-foam" role="img" aria-label="Photo of rolled foam packaging and building products" style="left:70px;top:1021px;width:277px;height:109px;border-radius:4px"></div>

  <!-- Middle column -->
  <div class="abs art art-yard" role="img" aria-label="Illustration of a recycling bin with plastic bottles in a landscape" style="left:417px;top:807px;width:113px;height:75px"></div>
  <div class="abs art art-fleet" role="img" aria-label="Illustration of a collection truck with sorting bins" style="left:566px;top:806px;width:174px;height:58px"></div>
  <div class="abs step bar gold" style="left:376px;top:894px;width:277px;height:40px">EXTRUDED RIGID PS PELLET</div>
  <div class="abs step bar olive" style="left:376px;top:972px;width:277px;height:40px">END MARKET APPLICATIONS</div>
  <div class="abs art art-pellets" role="img" aria-label="Photo of coloured recycled plastic pellets" style="left:375px;top:1018px;width:277px;height:163px;border-radius:4px"></div>

  <!-- Connectors -->
  <svg class="links" width="848" height="1200" viewBox="0 0 848 1200" aria-hidden="true">
    <defs>
      <marker id="head" viewBox="0 0 10 10" refX="5" refY="5" markerWidth="5" markerHeight="5" orient="auto">
        <path d="M0,0 L10,5 L0,10 z" fill="var(--arrow)"/>
      </marker>
      <marker id="tip" viewBox="0 0 10 10" refX="8" refY="5" markerWidth="5" markerHeight="5" orient="auto">
        <path d="M0,1 L9,5 L0,9 z" fill="var(--ink)"/>
      </marker>
    </defs>
    <g fill="none" stroke="var(--ink)" stroke-width="1" stroke-dasharray="4 3">
      <path d="M424 28 V84" marker-end="url(#tip)"/>
      <path d="M159 66 V59.5 H691 V66"/>
      <path d="M158 131 V148 M100 164 V148 H226 V164" marker-end="url(#tip)"/>
      <path d="M100 148 V164" marker-end="url(#tip)"/>
      <path d="M691 131 V148 M632 164 V148 H757 V164" marker-end="url(#tip)"/>
      <path d="M632 148 V164" marker-end="url(#tip)"/>
      <path d="M240 446 V459 M129 486 V465 H350 V486" marker-end="url(#tip)"/>
      <path d="M129 465 V486" marker-end="url(#tip)"/>
      <path d="M643 580 V603 M531 632 V609 H753 V632" marker-end="url(#tip)"/>
      <path d="M531 609 V632" marker-end="url(#tip)"/>
    </g>
    <g fill="var(--panel)" stroke="var(--ink)" stroke-width="1">
      <circle cx="158" cy="148" r="5"/>
      <circle cx="691" cy="148" r="5"/>
      <circle cx="240" cy="465" r="5"/>
      <circle cx="643" cy="609" r="5"/>
    </g>
    <g fill="none" stroke="var(--ink)" stroke-width="2.2" marker-end="url(#head)">
      <path d="M422 236 V284"/>
      <path d="M401 335 V360"/>
      <path d="M645 469 V503"/>
      <path d="M645 703 V740"/>
      <path d="M211 607 V640"/>
      <path d="M211 821 V858"/>
      <path d="M211 915 V960"/>
      <path d="M516 938 V967"/>
      <path d="M473 797 V730 H393 V620"/>
      <path d="M209 1139 V1164 H22 V315 H345"/>
      <path d="M834 315 V772 H797"/>
      <path d="M834 315 H506"/>
    </g>
  </svg>

</div>
</body>
</html>
```